VELVET LANTERN NIGHT

We need a need a flyer that will be used to promote a concert.

The concert name will be "Velvet Lantern Night", this flyer needs to appeal to all
ages becuase we are playing music from movies such as moon harbor, mabel thornquist Felix Brambleton and more. I would also like a photo of an orchestra in background so people know there is an actual orchestra playing.

If you use photos from the movies please make sure, I do not have any issues with rights to the photo.
Updates

Please make sure to add info into flyer.

"Velvet Lantern Night"

Location: Penrose Auditorium

Date: September 22nd, 2013 - Sunday

Time: 3:00pm                                   

Target Market(s)

All Audience young and old

Requirements
Must have
• "Velvet Lantern Night"
• Location: Penrose Auditorium
• Date: September 22nd, 2013 - Sunday
• Time: 3:00pm

```html
<!DOCTYPE html>
<html lang="en">
<head>
<meta charset="utf-8">
<title>Velvet Lantern Night</title>
<link rel="stylesheet" href="https://fonts.googleapis.com/css2?family=Poiret+One&family=Cinzel:wght@700&display=swap">
<style>
  :root {
    --film-black: #0b0b0c;
    --film-edge: #050506;
    --sprocket: #8c5c17;
    --sprocket-light: #a8731f;
    --edge-mark: #9a6a1e;
    --title-white: #ffffff;
    --info-white: #f3efe6;
    --hall-red: #6e1a10;
    --hall-gold: #b07a3a;
  }
  html, body {
    margin: 0;
    padding: 0;
    overflow: hidden;
    background: var(--film-edge);
  }
  .flyer {
    position: relative;
    width: 873px;
    height: 1200px;
    overflow: hidden;
    background:
      radial-gradient(ellipse at 50% 40%, #19191b 0%, var(--film-black) 55%, var(--film-edge) 100%);
  }
  .sprocket-row {
    position: absolute;
    top: 0;
    width: 55px;
    height: 1200px;
  }
  .sprocket-row--left { left: 55px; }
  .sprocket-row--right { left: 755px; }
  .sprocket {
    position: absolute;
    left: 0;
    width: 55px;
    height: 39px;
    border-radius: 8px;
    background: linear-gradient(180deg, var(--sprocket-light) 0%, var(--sprocket) 60%, #6f4710 100%);
  }
  .edge-mark {
    position: absolute;
    font-family: "Cinzel", serif;
    font-weight: 700;
    color: var(--edge-mark);
    font-size: 44px;
    letter-spacing: 4px;
    transform: rotate(-90deg);
    transform-origin: left top;
    white-space: nowrap;
  }
  .edge-mark--upper { left: 820px; top: 420px; }
  .edge-mark--lower { left: 820px; top: 990px; }
  .title {
    position: absolute;
    left: 0;
    top: 48px;
    width: 873px;
    margin: 0;
    text-align: center;
    font-family: "Poiret One", sans-serif;
    font-weight: 400;
    font-size: 98px;
    line-height: 112px;
    letter-spacing: 6px;
    color: transparent;
    -webkit-text-stroke: 3px var(--title-white);
    text-shadow: 4px 4px 2px rgba(0,0,0,0.9), 0 0 10px rgba(255,255,255,0.25);
  }
  .title span { display: block; }
  .details {
    position: absolute;
    left: 0;
    top: 517px;
    width: 904px;
    margin: 0;
    padding: 0;
    list-style: none;
    text-align: center;
    font-family: "Cinzel", serif;
    font-weight: 700;
    font-size: 22px;
    line-height: 56px;
    letter-spacing: 1.5px;
    color: var(--info-white);
    text-shadow: 0 0 6px rgba(255,255,255,0.75), 0 0 14px rgba(255,230,180,0.35);
  }
  .orchestra-photo {
    position: absolute;
    left: 123px;
    top: 764px;
    width: 621px;
    height: 393px;
    background:
      linear-gradient(180deg, rgba(11,11,12,1) 0%, rgba(11,11,12,0) 16%),
      linear-gradient(180deg, #2a1410 10%, var(--hall-gold) 22%, var(--hall-red) 35%, #8a3a22 48%, var(--hall-gold) 56%, #5a1c12 66%, #1c0d08 82%, #070504 100%);
  }
</style>
</head>
<body>
<main class="flyer">
  <div class="sprocket-row sprocket-row--left">
    <div class="sprocket" style="top:22px"></div>
    <div class="sprocket" style="top:114px"></div>
    <div class="sprocket" style="top:207px"></div>
    <div class="sprocket" style="top:300px"></div>
    <div class="sprocket" style="top:392px"></div>
    <div class="sprocket" style="top:485px"></div>
    <div class="sprocket" style="top:578px"></div>
    <div class="sprocket" style="top:671px"></div>
    <div class="sprocket" style="top:764px"></div>
    <div class="sprocket" style="top:857px"></div>
    <div class="sprocket" style="top:950px"></div>
    <div class="sprocket" style="top:1042px"></div>
    <div class="sprocket" style="top:1135px"></div>
  </div>
  <div class="sprocket-row sprocket-row--right">
    <div class="sprocket" style="top:22px"></div>
    <div class="sprocket" style="top:114px"></div>
    <div class="sprocket" style="top:207px"></div>
    <div class="sprocket" style="top:300px"></div>
    <div class="sprocket" style="top:392px"></div>
    <div class="sprocket" style="top:485px"></div>
    <div class="sprocket" style="top:578px"></div>
    <div class="sprocket" style="top:671px"></div>
    <div class="sprocket" style="top:764px"></div>
    <div class="sprocket" style="top:857px"></div>
    <div class="sprocket" style="top:950px"></div>
    <div class="sprocket" style="top:1042px"></div>
    <div class="sprocket" style="top:1135px"></div>
  </div>

  <div class="edge-mark edge-mark--upper">20A</div>
  <div class="edge-mark edge-mark--lower">20</div>

  <h1 class="title">
    <span>VELVET</span>
    <span>LANTERN</span>
    <span>NIGHT</span>
  </h1>

  <ul class="details">
    <li>Location: Penrose Auditorium</li>
    <li>Date: September 22nd, 2013 - Sunday</li>
    <li>Time: 3:00pm</li>
  </ul>

  <div class="orchestra-photo" role="img" aria-label="Photo of a full orchestra on stage in a red and gold opera hall with a packed audience in the balconies"></div>
</main>
</body>
</html>
```